Creative flyer for small business IT services

We are an IT services company based in Western Australia. We're looking to expand our market share amongst small businesses and need a brochure/flyer designed to give them a good overview of why we can help them. The design and layout should be consistent with an existing company profile brochure (included) but please be creative. A comprehensive brief with copy and a rough layout is included.

Small Business

```html
<!DOCTYPE html>
<html lang="en">
<head>
<meta charset="utf-8">
<title>Northgate Tech – Small Business IT Solutions</title>
<link href="https://fonts.googleapis.com/css2?family=PT+Sans:ital,wght@0,400;0,700;1,700&family=PT+Sans+Narrow:wght@400;700&display=swap" rel="stylesheet">
<style>
:root{
  --red:#a3191f;
  --red-deep:#7d1015;
  --grey-dark:#555456;
  --grey-frame:#3c3c3e;
  --grey-text:#3a3a3a;
  --paper:#ffffff;
  --canvas:#eeeeee;
  --beige:#e9d3c6;
  --soil:#6b4427;
  --pink-soft:#f0c7c8;
}
*{margin:0;padding:0;box-sizing:border-box}
html,body{width:925px;height:1200px;overflow:hidden;background:var(--canvas)}
body{font-family:"PT Sans",Arial,sans-serif;color:var(--grey-text)}
.flyer{position:relative;width:925px;height:1200px;background:var(--paper);overflow:hidden}
.header-band{position:absolute;left:0;top:0;width:925px;height:320px}
.brand{position:absolute;left:48px;top:38px;width:140px}
.brand-square{width:132px;height:122px;background:var(--paper)}
.brand-name{margin-top:4px;font-size:19px;color:#e9a9ab;letter-spacing:.5px}
.title{position:absolute;left:205px;top:64px;font-family:"PT Sans Narrow",Arial,sans-serif;font-weight:700;font-size:56px;line-height:1;color:#fff;letter-spacing:.3px}
.hardware-photo{position:absolute;left:692px;top:150px;width:196px;height:140px;border-radius:6px;background:linear-gradient(135deg,#dcdcdc,#4a4a4a 60%,#1c1c1c)}
.headline{position:absolute;left:48px;top:296px;font-weight:700;font-size:53px;line-height:1;color:var(--red);letter-spacing:-.3px}
.subline{position:absolute;left:48px;top:352px;font-weight:700;font-size:38px;line-height:1;color:var(--grey-dark)}
.seedlings{position:absolute;left:120px;top:398px;width:760px;height:96px;background:linear-gradient(180deg,rgba(123,178,58,0) 0%,rgba(123,178,58,.55) 45%,var(--soil) 80%,#8a5a35 100%);border-radius:40px 40px 10px 10px}
.intro-box{position:absolute;top:500px;height:170px;padding:12px 16px}
.intro-red{left:48px;width:382px;background:var(--red);color:#fff}
.intro-grey{left:438px;width:440px;background:var(--grey-dark);color:#fff;border-radius:0 8px 8px 0}
.intro-box h2{font-size:21px;font-weight:400;line-height:1.15}
.intro-red p{margin-top:14px;font-size:12.5px;line-height:1.32;color:var(--pink-soft);text-align:justify}
.reasons{list-style:none;margin-top:10px}
.reasons li{font-size:14.5px;font-weight:700;line-height:1.2;margin-bottom:8px;padding-left:20px;position:relative}
.reasons li::before{content:"";position:absolute;left:0;top:4px;width:10px;height:10px;border-radius:50%;background:#fff}
.services{position:absolute;left:0;top:678px;width:925px;height:320px;background:linear-gradient(180deg,var(--beige) 0%,#f7ece5 35%,#fff 100%)}
.service{position:absolute;top:18px}
.service h3{font-size:17px;font-weight:700;line-height:1.2;color:var(--red);margin-bottom:10px}
.service p{font-family:"PT Sans Narrow",Arial,sans-serif;font-size:12px;line-height:12.6px;text-align:justify;margin-bottom:8px}
.s1{left:48px;width:200px}
.s2{left:266px;width:214px}
.s3{left:498px;width:196px}
.s4{left:712px;width:166px}
.footer-band{position:absolute;left:0;top:1118px;width:925px;height:82px;background:var(--red)}
.testimonials{position:absolute;left:40px;top:992px;width:845px;height:132px;background:#fff;border:5px solid var(--grey-frame);border-top-width:20px;border-radius:10px;padding:6px 14px;display:flex;gap:26px;font-size:12px;line-height:1.28}
.testimonials-tab{position:absolute;left:50%;top:-26px;transform:translateX(-50%);background:var(--grey-frame);color:#fff;font-style:italic;font-weight:700;font-size:19px;padding:0 18px;border-radius:8px 8px 0 0;height:26px;line-height:26px}
.testimonials .col{flex:1;text-align:justify}
.testimonials p+p{margin-top:7px}
.contact{position:absolute;left:0;top:1136px;width:925px;text-align:center;color:#fff}
.contact-line{display:flex;justify-content:center;gap:18px;align-items:center}
.contact-line.small{font-size:13px}
.contact-line.large{margin-top:8px;font-size:17px;font-weight:700;letter-spacing:.5px}
.contact-line.large .phone{font-size:20px}
.dot{display:inline-block;width:9px;height:7px;border-radius:50%;background:#fff;margin-right:6px;vertical-align:middle}
</style>
</head>
<body>
<div class="flyer">
  <svg class="header-band" viewBox="0 0 925 320" aria-hidden="true">
    <defs>
      <linearGradient id="bandFill" x1="0" y1="0" x2="0" y2="1">
        <stop offset="0" stop-color="#b0242a"/>
        <stop offset="1" stop-color="#8e141a"/>
      </linearGradient>
    </defs>
    <path d="M0 0H925V205C700 248 380 205 0 300Z" fill="url(#bandFill)"/>
    <path d="M0 262C360 200 660 232 925 190" fill="none" stroke="#d54a4e" stroke-width="5" opacity=".8"/>
    <path d="M0 290C380 230 690 252 925 212" fill="none" stroke="#6f0e12" stroke-width="3" opacity=".7"/>
  </svg>

  <div class="brand">
    <div class="brand-square"></div>
    <div class="brand-name">northgatetech</div>
  </div>
  <h1 class="title">SMALL BUSINESS IT SOLUTIONS</h1>
  <div class="hardware-photo" role="img" aria-label="Photo of a desktop computer with monitor, tower, keyboard and mouse"></div>

  <div class="headline">Small business. Big ideas.</div>
  <div class="subline">We’ll help your business grow.</div>
  <div class="seedlings" role="img" aria-label="Row of seedlings growing taller from small mounds of soil"></div>

  <section class="intro-box intro-red">
    <h2>We help small businesses get ahead of the pack.</h2>
    <p>You’ve always got more to do. In a small business, the last thing you need is another hat to wear. You shouldn’t need to become a computer engineer to keep your business running smoothly. Say goodbye to IT headaches - our mission is to make your life easier.</p>
  </section>
  <section class="intro-box intro-grey">
    <h2>Here’s why small businesses love Northgate Tech:</h2>
    <ul class="reasons">
      <li>We’re small business IT experts</li>
      <li>We speak plain English and won’t waste your time</li>
      <li>We care about our relationships</li>
      <li>We worry about IT so you don’t have to</li>
    </ul>
  </section>

  <section class="services">
    <div class="service s1">
      <h3>Support Services</h3>
      <p>Say goodbye to IT interruptions, slow services, confusing jargon and inexplicable errors. We have solutions to your IT problems, and packages to suit every budget. We can even come to your workplace. If you run into a problem or need something done, just contact our Service Desk.</p>
      <p>Whether you have a single computer or a big team with complex requirements, our expert team can assist. We’ll give you an entire IT department for a fraction of the cost.</p>
    </div>
    <div class="service s2">
      <h3>Monitoring &amp; Backup</h3>
      <p>Most of us insure our cars and homes, yet small businesses often don’t protect themselves from the kind of disaster that strikes every day. Could your business recover from the complete loss of every electronic file-financial records, legal documents, customer information, intellectual property, archives, emails and more?</p>
      <p>Our Monitor &amp; Protect solutions keep you safe from physical threats like theft, fire and floods, but also from electronic threats like viruses and hackers. Best of all - it happens automatically, so you can relax.</p>
    </div>
    <div class="service s3">
      <h3>Hardware &amp; Software</h3>
      <p>Every business needs the right tools for the job. We supply world class hardware and software products from Veltrix, Corvane, Datamere, Orchardline, Linkmast, Pixelforge, Voltguard and many more. Our strong partnerships and buying power mean we can save you money.</p>
      <p>From a single keyboard to an entire infrastructure, we always take the time to help you select the right products.</p>
    </div>
    <div class="service s4">
      <h3>Audit</h3>
      <p>It helps to know where you stand.</p>
      <p>Get a clearer picture of your IT systems with our obligation-free IT audit and consultation.</p>
      <p>Contact us today and we’ll provide you with expert insights into how your business can benefit from today’s amazing technology.</p>
    </div>
  </section>

  <div class="footer-band"></div>

  <section class="testimonials">
    <div class="testimonials-tab">Testimonials</div>
    <div class="col">
      <p>Don’t just take our word for it! Here’s what some satisfied customers have to say about Northgate Tech:</p>
      <p>• “We are pleased to have Northgate Tech as part of our team. I recommend Northgate Tech for any business seeking a trustworthy, reliable and effective IT service provider.” Marcus Hale, Coastline Imaging</p>
    </div>
    <div class="col">
      <p>• “Northgate Tech’s expertise has allowed us to test, analyse and improve the reliability and performance of our application, further improving the health and financial status of our business.” Laura Finch, Gradebook Pty Ltd</p>
    </div>
  </section>

  <footer class="contact">
    <div class="contact-line small">
      <span><span class="dot"></span>Level 12, 80 Harbour Row Perth WA 6000</span>
      <span><span class="dot"></span>sales@northgatetech.com.au</span>
    </div>
    <div class="contact-line large">
      <span><span class="dot"></span>www.northgatetech.com.au</span>
      <span class="phone"><span class="dot"></span>1300 555 018</span>
    </div>
  </footer>
</div>
</body>
</html>
```